Vital Years Forward an age management group needs a modern looking website developed asap

Vital Years Forward is an age management group lead by a board certified medical doctor (who also specializes in age management medicine) and a 7th degree black belt jiu-jitsu master. Both have joined forces to create a unique doctor supervised anti-aging medical, nutritional, hormonal, exercise protocol never seen before.
This marriage between medicine and athleticism will create the worlds first complete anti-aging program designed for anyone wishing to remain as healthy and as young for as long as possible.

Our Mission and Vision: "To provide clients cutting edge anti aging programs and protocols designed to "turn-back-the-clock-one-second-at-a-time. Let's all Vital Years Forward..together!"

Vital Years Forward's program consists of 6 unique tiers/platforms each encompassing a specific need.
The 6 tiers are:
1. Apex Vigor: A medical doctor supervised unique and proprietary hormone optimization program and protocol developed by a board certified medical doctor trained by Voralithe ( a world leader in age management medicine) who has practiced age management medicine for the past 7 years
2. Apex Trim: A medical doctor supervised unique and proprietary weight management program and protocol developed by a published medical doctor who's diet book "Brighter Mornings: A Kitchen Reset" was just launched
3.Apex Move: A master athlete supervised training program and protocol, with access to a large proprietary exercise video databank developed by a 7th degree black belt jiu-jitsu master.
4. Apex Plate: A chef driven and supervised home delivered healthy meals. Each meal is made from scratch, and is specifically tailored and targeted according to each patient's specific needs.
5. ApexMegaNutri: A doctor formulated-master athlete approved most complete multi vitamin-mineral-anti-oxidant and supplement pack available on the market today. ApexMegaNutri is: made in the USA, and FDA approved vitamin factory, gluten free, sugar free, and artificial color free.
6. Apex Study: A unique CME approved teaching workshop intended for those physicians who lack expertise in age management but want to become proficient in the art of hormone optimization and age management medicine. The 2-day workshop is held twice monthly on Saturday and Sunday in sunny Florida.

This is our scope and goal.
We want to become the leaders in age management medicine by being the first to unite doctors-athletes-chefs-nutritionist together in an effort to deliver the most advanced most cutting edge programs and protocols so we may all : VITAL YAERS FORWARD!

We already have the logo for Vital years forward.
Please keep in mind the following:
1. Apex vigorous should be in green and black
2. Apex trim should be in purple and black
3. Apex move in orange and black
4. Apx plate in yellow and black
5. ApexMegaNurti in red and black
6. Apex study in gray and black

Target Market(s)

Adults Males and females wishing to remain as healthy and as young for as long as possible
Obese and overweight adults males and females
Athletes males and females
Young obese and overweight males and females
ALL can be from any country!

Industry/Entity Type

Health And Wellness

Coding

Coded - Design and coding required

Number of Pages Required

5+ page

Requirements
Must have
• The front page must have our mission statement as well as the 6 tiers/platforms displayed (Apex Vigor, Apex Trim, Apex Move, Apex Plate, ApexMegaNutri, Apex Study) and each platform when "cliked on" should open up in its own unique page.
• The capability for clients to log on to any of the pages using assigned usernames and passwords.
• The capability of check out (credit cards, paypal) from any of the pages. EX the client may want to buy ApexMegaNutri. He/She would click on the main page then click on ApexMeganutri page and choose to buy the vitamin. Same For the rest: He/she may want to buy the weight loss program (apex trim), or the Hormone program (apex vigor) or the food delivered home (apex Plate) or apex move (access to the exercise video databank) or attend the workshop (buy the teaching program..BUT this will ONLY be accessible if the client is a medical doctor and has a valid medical license).
• Also the client may want to have full access to ALL the 6 tiers, thus on the FRONT page we need a checkout with "full access to tiers"
• Also we need to make sure no videos are downloade but only viewed. we need to have this safety built in.
• Also we nee to be able to keep track of emails and have stats. and any email inquiry must be diverted to my iphone.
Nice to have
• Modern look with pop-ups and graphics and iphone and android capability
Should not have
• nothing explicit

```html
<!DOCTYPE html>
<html lang="en">
<head>
<meta charset="utf-8">
<title>Vital Years Forward</title>
<link href="https://fonts.googleapis.com/css2?family=Lato:wght@300;400;700&family=Merriweather:ital,wght@1,300;1,400&family=Open+Sans:wght@400;600&display=swap" rel="stylesheet">
<style>
:root{
  --green:#8dc63f;
  --green-dark:#76b02a;
  --ink:#222;
  --text:#555;
  --muted:#777;
  --band:#f2f2f2;
  --line:#e2e2e2;
  --footer:#555;
  --footer-line:#6a6a6a;
  --vigor:#8dc63f;
  --trim:#7a0e94;
  --move:#ff6600;
  --plate:#ffff00;
  --nutri:#ff0000;
  --study:#777;
}
*{margin:0;padding:0;box-sizing:border-box}
html,body{width:1200px;height:2273px;overflow:hidden}
body{position:relative;background:#fff;font-family:"Open Sans",sans-serif;color:var(--text)}
.abs{position:absolute}

/* header */
.site-header{position:absolute;left:0;top:0;width:1200px;height:121px;background:#fff;border-top:3px solid var(--green);box-shadow:0 1px 4px rgba(0,0,0,.08);z-index:2}
.brand{position:absolute;left:133px;top:30px;width:124px;text-align:center}
.brand-mark{display:block;margin:0 auto 6px;width:44px;height:44px;border:3px solid var(--green);border-radius:50%}
.brand-name{font-family:"Lato",sans-serif;font-weight:700;font-size:13px;color:#3aa6c9;white-space:nowrap}
.btn-checkout{position:absolute;left:989px;top:18px;width:80px;height:29px;background:var(--green);color:#fff;font-family:"Lato",sans-serif;font-size:11px;line-height:29px;text-align:center;border-radius:2px}
.main-nav{position:absolute;top:86px;left:0;width:1200px;font-family:"Lato",sans-serif;font-size:11px;color:#333}
.main-nav a{position:absolute;text-decoration:none;color:#333;white-space:nowrap}
.main-nav a.active{color:var(--green)}
.main-nav a.active::after{content:"";position:absolute;left:50%;top:30px;margin-left:-11px;border:6px solid transparent;border-bottom:6px solid var(--green);width:10px}

/* hero */
.hero{position:absolute;left:0;top:121px;width:1200px;height:455px;background:linear-gradient(90deg,#b9c6d3 0%,#c6d1dc 30%,#d6dee6 60%,#e4e8ec 100%)}
.hero-photo{position:absolute;left:363px;top:0;width:837px;height:455px;background:radial-gradient(ellipse at 72% 45%,#e8c9b4 0%,#d9b8a4 18%,rgba(220,226,232,0) 45%),radial-gradient(ellipse at 42% 60%,#f2f2f2 0%,#e6ebe3 18%,rgba(220,226,232,0) 38%),linear-gradient(90deg,#cdd6df,#e6e9ec)}
.hero-title{position:absolute;left:130px;top:112px;font-family:"Lato",sans-serif;font-weight:300;font-size:50px;color:#2a2a2a;letter-spacing:-.5px}
.hero-lead{position:absolute;left:133px;top:196px;width:360px;font-family:"Merriweather",serif;font-style:italic;font-size:12.5px;line-height:21px;color:#222}
.btn-hero{position:absolute;left:133px;top:268px;width:155px;height:50px;background:linear-gradient(#9fd24d,#7dbb2c);color:#fff;font-family:"Lato",sans-serif;font-size:14px;line-height:50px;text-align:center;border-radius:2px}
.hero-dots{position:absolute;left:134px;top:346px;display:flex;gap:10px}
.hero-dots span{width:12px;height:12px;border-radius:50%;background:#a9b3bd}
.hero-dots span.on{background:var(--green)}

/* tiers */
.tier{position:absolute;width:300px}
.tier-icon{position:absolute;left:0;top:0;width:74px;height:74px;border-radius:50%;display:flex;align-items:center;justify-content:center}
.tier-title{position:absolute;left:89px;top:6px;font-family:"Lato",sans-serif;font-size:20px;color:#222;white-space:nowrap}
.tier-text{position:absolute;left:89px;top:42px;width:203px;font-size:11.5px;line-height:19px;color:var(--muted);text-align:justify}

/* mission */
.mission{position:absolute;left:0;top:961px;width:1200px;height:429px;background:var(--band);border-top:1px solid var(--line);border-bottom:1px solid var(--line)}
.section-title{font-family:"Lato",sans-serif;font-weight:400;font-size:29px;color:#222}
.mission .section-title{position:absolute;left:132px;top:71px}
.mission-text{position:absolute;left:133px;top:145px;width:510px;font-family:"Merriweather",serif;font-style:italic;font-weight:300;font-size:19.5px;line-height:33.5px;color:#666;text-align:justify}
.mission-text em{color:var(--green);font-style:italic}
.video-frame{position:absolute;left:681px;top:65px;width:388px;height:272px;background:#e6e6e6;border:1px solid #d6d6d6;padding:10px;box-shadow:0 1px 3px rgba(0,0,0,.12)}
.video-still{position:relative;width:100%;height:100%;background:radial-gradient(ellipse at 80% 35%,#e4c3b0 0%,rgba(200,220,228,0) 35%),linear-gradient(90deg,#a9cbd8,#cfe2ea 60%,#e8eef0)}
.play-btn{position:absolute;left:155px;top:93px;width:64px;height:64px}

/* programs */
.programs .section-title{position:absolute;left:0;top:1436px;width:1200px;text-align:center}
.program-card{position:absolute;top:1518px;width:296px;height:376px;background:#fff;border:1px solid #e4e4e4;box-shadow:0 2px 5px rgba(0,0,0,.15)}
.program-photo{position:absolute;left:0;top:0;width:294px;height:194px}
.photo-doctor{background:linear-gradient(90deg,#dfe8ee,#f3f5f6 45%,#f5c36b 80%,#f0a03a)}
.photo-kitchen{background:linear-gradient(180deg,#f0ece6 0%,#e8d9c8 45%,#9cc45a 75%,#6aa23a)}
.photo-fruit{background:radial-gradient(ellipse at 50% 30%,#e4c3ad 0%,rgba(170,200,120,0) 30%),linear-gradient(180deg,#b9d48d,#d3e3a8 60%,#e89a3c)}
.date-badge{position:absolute;right:0;top:128px;width:56px;height:66px;background:var(--green);color:#fff;text-align:center;font-family:"Lato",sans-serif}
.date-badge b{display:block;font-size:22px;font-weight:400;padding-top:9px;line-height:24px}
.date-badge small{display:block;font-size:10px;margin-top:3px}
.program-title{position:absolute;left:17px;top:218px;font-family:"Lato",sans-serif;font-size:20px;color:var(--green);white-space:nowrap}
.program-text{position:absolute;left:17px;top:252px;width:262px;font-size:11px;line-height:19px;color:#555;text-align:justify}
.read-more{position:absolute;left:17px;top:331px;display:flex;align-items:center;gap:13px;font-family:"Lato",sans-serif;font-size:15px;color:var(--green)}
.read-more svg{width:24px;height:24px}

/* footer */
.site-footer{position:absolute;left:0;top:1966px;width:1200px;height:307px;background:var(--footer);color:#fff}
.footer-brand{position:absolute;left:130px;top:30px;width:130px;text-align:center}
.footer-brand .brand-mark{border-color:#fff;width:48px;height:48px;margin-bottom:6px}
.footer-brand .brand-name{color:#fff;font-size:13px}
.social{position:absolute;left:133px;top:124px;display:flex;gap:7px}
.social span{width:30px;height:30px;border:2px solid #fff;border-radius:50%}
.pay-box{position:absolute;left:133px;top:174px;width:180px;height:40px;border:2px solid #fff;background:#444;display:flex;align-items:flex-end;gap:4px;padding:0 4px 5px}
.pay-box span{width:30px;height:15px;background:#ddd;border-radius:1px}
.pay-box span.wide{position:absolute;left:8px;top:4px;width:70px;height:12px;background:#bbb}
.footer-col{position:absolute;top:32px}
.footer-col h4{font-family:"Lato",sans-serif;font-weight:700;font-size:14px;letter-spacing:.3px;margin-bottom:14px}
.quick-links{left:406px}
.quick-links li{list-style:none;font-size:11px;line-height:20.5px}
.newsletter{left:615px}
.newsletter p{font-size:11px;color:#ddd;margin-bottom:16px}
.email-field{width:196px;height:33px;background:#777;border:1px solid #888;font-size:10.5px;line-height:31px;padding-left:12px;color:#fff}
.btn-subscribe{margin-top:21px;width:83px;height:25px;background:var(--green);font-size:10px;line-height:25px;text-align:center}
.contact{left:884px}
.contact li{list-style:none;display:flex;gap:13px;font-size:11px;line-height:15px;margin-bottom:12px;width:180px}
.contact svg{flex:none;width:13px;height:13px;margin-top:1px}
.contact u{color:#fff}
.footer-bottom{position:absolute;left:133px;top:246px;width:936px;border-top:1px solid var(--footer-line);text-align:center;font-size:10.5px;padding-top:20px}
</style>
</head>
<body>

<header class="site-header">
  <div class="brand"><span class="brand-mark"></span><span class="brand-name">Vital Years Forward</span></div>
  <div class="btn-checkout">CHECK OUT</div>
  <nav class="main-nav">
    <a class="active" style="left:599px">HOME</a>
    <a style="left:679px">ABOUT US</a>
    <a style="left:778px">SERVICES</a>
    <a style="left:871px">FAQ</a>
    <a style="left:939px">NEWS</a>
    <a style="left:1017px">CONTACT</a>
  </nav>
</header>

<section class="hero">
  <div class="hero-photo" role="img" aria-label="Woman eating a bowl of fresh salad with vegetables falling into it"></div>
  <h1 class="hero-title">HEALTHY FOOD</h1>
  <p class="hero-lead">Lorem ipsum dolor sit amet, consectetur adipiscing elit, sed do eiusmod tempor incididunt</p>
  <div class="btn-hero">VIEW DETAILS</div>
  <div class="hero-dots"><span class="on"></span><span></span><span></span></div>
</section>

<section class="tiers">
  <div class="tier" style="left:133px;top:633px">
    <div class="tier-icon" style="background:var(--vigor)"><svg width="40" height="36" viewBox="0 0 40 36"><path d="M20 34 4 18A9 9 0 0 1 20 6a9 9 0 0 1 16 12Z" fill="#111"/><path d="M2 18h11l3-6 4 12 3-8 2 2h13" fill="none" stroke="#8dc63f" stroke-width="2.5"/></svg></div>
    <h3 class="tier-title">APEX VIGOROUS</h3>
    <p class="tier-text">Lorem ipsum dolor sit amet, consectetur adipiscing elit, sed do eiusmod tempor incididunt</p>
  </div>
  <div class="tier" style="left:454px;top:633px">
    <div class="tier-icon" style="background:var(--trim)"><svg width="34" height="34" viewBox="0 0 34 34"><circle cx="17" cy="10" r="8" fill="#111"/><path d="M3 34c0-10 6-15 14-15s14 5 14 15Z" fill="#111"/></svg></div>
    <h3 class="tier-title">APEX TRIM</h3>
    <p class="tier-text">Lorem ipsum dolor sit amet, consectetur adipiscing elit, sed do eiusmod tempor incididunt</p>
  </div>
  <div class="tier" style="left:774px;top:633px">
    <div class="tier-icon" style="background:var(--move)"><svg width="42" height="24" viewBox="0 0 42 24"><rect x="6" y="2" width="7" height="20" rx="1" fill="#111"/><rect x="29" y="2" width="7" height="20" rx="1" fill="#111"/><rect x="1" y="6" width="4" height="12" fill="#111"/><rect x="37" y="6" width="4" height="12" fill="#111"/><rect x="13" y="10" width="16" height="4" fill="#111"/></svg></div>
    <h3 class="tier-title">APEX MOVE</h3>
    <p class="tier-text">Lorem ipsum dolor sit amet, consectetur adipiscing elit, sed do eiusmod tempor incididunt</p>
  </div>
  <div class="tier" style="left:133px;top:777px">
    <div class="tier-icon" style="background:var(--plate)"><svg width="30" height="38" viewBox="0 0 30 38"><path d="M15 9C6 7 1 14 2 23c1 9 7 14 13 14s12-5 13-14C29 14 24 7 15 9Z" fill="#111"/><path d="M15 9c0-4 2-7 5-8" stroke="#111" stroke-width="3" fill="none"/></svg></div>
    <h3 class="tier-title">APEX PLATE</h3>
    <p class="tier-text">Lorem ipsum dolor sit amet, consectetur adipiscing elit, sed do eiusmod tempor incididunt</p>
  </div>
  <div class="tier" style="left:454px;top:777px">
    <div class="tier-icon" style="background:var(--nutri)"><svg width="40" height="32" viewBox="0 0 40 32"><path d="M4 10 30 2l6 8L10 30Z" fill="none" stroke="#111" stroke-width="3"/><path d="M10 12l3 5M15 10l2 4M20 9l3 5M25 7l2 4" stroke="#111" stroke-width="2"/></svg></div>
    <h3 class="tier-title">APEX MEGANUTRI</h3>
    <p class="tier-text">Lorem ipsum dolor sit amet, consectetur adipiscing elit, sed do eiusmod tempor incididunt</p>
  </div>
  <div class="tier" style="left:774px;top:777px">
    <div class="tier-icon" style="background:var(--study)"><svg width="44" height="32" viewBox="0 0 44 32"><path d="M22 6C16 2 8 2 2 4v26c6-2 14-2 20 2 6-4 14-4 20-2V4c-6-2-14-2-20 2Z" fill="#111"/><path d="M22 7v24M6 8c5-1 10-1 13 1v18c-4-2-9-2-13-1ZM38 8c-5-1-10-1-13 1v18c4-2 9-2 13-1Z" fill="#777" stroke="#111"/></svg></div>
    <h3 class="tier-title">APEX STUDY</h3>
    <p class="tier-text">Lorem ipsum dolor sit amet, consectetur adipiscing elit, sed do eiusmod tempor incididunt</p>
  </div>
</section>

<section class="mission">
  <h2 class="section-title">OUR MISSION AND VISION</h2>
  <p class="mission-text">To provide clients cutting edge anti aging programs and protocols designed to <em>"turn-back-the-clock-one-second-at-a-time. Let's all Vital Years Forward..together!</em></p>
  <div class="video-frame">
    <div class="video-still" role="img" aria-label="Video still of a doctor presenting vitamins and fresh fruit">
      <svg class="play-btn" viewBox="0 0 64 64"><circle cx="32" cy="32" r="29" fill="rgba(255,255,255,.15)" stroke="#444" stroke-width="3"/><path d="M25 18v28l22-14Z" fill="#444"/></svg>
    </div>
  </div>
</section>

<section class="programs">
  <h2 class="section-title">OUR PROGRAM</h2>
  <article class="program-card" style="left:133px">
    <div class="program-photo photo-doctor" role="img" aria-label="Doctor with citrus fruit and a measuring tape"></div>
    <div class="date-badge"><b>01</b><small>AUG</small></div>
    <h3 class="program-title">MEDICAL DOCTOR</h3>
    <p class="program-text">Lorem ipsum dolor sit amet, consectetur adipiscing elit, sed do eiusmod tempor incididunt ut labore et dolore magna aliqua.</p>
    <div class="read-more"><svg viewBox="0 0 24 24"><circle cx="12" cy="12" r="10.5" fill="none" stroke="#8dc63f" stroke-width="1.5"/><path d="M10 7l5 5-5 5" fill="none" stroke="#8dc63f" stroke-width="1.5"/></svg>READ MORE</div>
  </article>
  <article class="program-card" style="left:452px">
    <div class="program-photo photo-kitchen" role="img" aria-label="Fresh vegetables being chopped on a kitchen board"></div>
    <div class="date-badge"><b>01</b><small>AUG</small></div>
    <h3 class="program-title">MEDICAL DOCTOR</h3>
    <p class="program-text">Lorem ipsum dolor sit amet, consectetur adipiscing elit, sed do eiusmod tempor incididunt ut labore et dolore magna aliqua.</p>
    <div class="read-more"><svg viewBox="0 0 24 24"><circle cx="12" cy="12" r="10.5" fill="none" stroke="#8dc63f" stroke-width="1.5"/><path d="M10 7l5 5-5 5" fill="none" stroke="#8dc63f" stroke-width="1.5"/></svg>READ MORE</div>
  </article>
  <article class="program-card" style="left:772px">
    <div class="program-photo photo-fruit" role="img" aria-label="Smiling woman behind a table of fresh fruit"></div>
    <div class="date-badge"><b>01</b><small>AUG</small></div>
    <h3 class="program-title">MEDICAL DOCTOR</h3>
    <p class="program-text">Lorem ipsum dolor sit amet, consectetur adipiscing elit, sed do eiusmod tempor incididunt ut labore et dolore magna aliqua.</p>
    <div class="read-more"><svg viewBox="0 0 24 24"><circle cx="12" cy="12" r="10.5" fill="none" stroke="#8dc63f" stroke-width="1.5"/><path d="M10 7l5 5-5 5" fill="none" stroke="#8dc63f" stroke-width="1.5"/></svg>READ MORE</div>
  </article>
</section>

<footer class="site-footer">
  <div class="footer-brand"><span class="brand-mark"></span><span class="brand-name">Vital Years Forward</span></div>
  <div class="social"><span></span><span></span><span></span><span></span><span></span></div>
  <div class="pay-box"><span class="wide"></span><span></span><span></span><span></span><span></span><span></span></div>

  <div class="footer-col quick-links">
    <h4>QUICK LINKS</h4>
    <ul><li>Home</li><li>About us</li><li>Services</li><li>FAQ</li><li>Programs</li><li>Contact</li></ul>
  </div>
  <div class="footer-col newsletter">
    <h4>NEWSLETTER</h4>
    <p>Sign Up for Our Newsletter &amp; Promotion</p>
    <div class="email-field">Enter Your email Id</div>
    <div class="btn-subscribe">SUBSCRIBE</div>
  </div>
  <div class="footer-col contact">
    <h4>CONTACT US</h4>
    <ul>
      <li><svg viewBox="0 0 13 13"><path d="M1 4c0-2 2-3 5.5-3S12 2 12 4v1H9V3.5H4V5H1Z M2 6h9l1 6H1Z" fill="#fff"/></svg>1800 555 0199</li>
      <li><svg viewBox="0 0 13 13"><rect x="3" y="1" width="7" height="4" fill="#fff"/><rect x="1" y="5" width="11" height="5" fill="#fff"/><rect x="3" y="8" width="7" height="4" fill="#fff" stroke="#555"/></svg>1800 555 0199</li>
      <li><svg viewBox="0 0 13 13"><rect x="1" y="2.5" width="11" height="8" fill="#fff"/><path d="M1 3l5.5 4.5L12 3" fill="none" stroke="#555"/></svg><u>hello@vitalyearsforward.example</u></li>
      <li><svg viewBox="0 0 13 13"><path d="M6.5 12S2 7 2 4.5a4.5 4.5 0 0 1 9 0C11 7 6.5 12 6.5 12Z" fill="#fff"/><circle cx="6.5" cy="4.5" r="1.6" fill="#555"/></svg>#2868 Lorem ipsum dolor sit amet, consectetur</li>
    </ul>
  </div>
  <div class="footer-bottom">Copyright © 2016 Vital Years Forward. All right Reserved.</div>
</footer>

</body>
</html>
```